Business Cards for new orthopaedic surgery practice

My husband and I are starting our own orthopaedic surgery practice. We are looking for a business card that is uniform, but one will have my name/title and the other will have his. You can just create one design with my name on it for now. But when I choose your design as the winning design I will ask that you add another copy with his name/title.

We are looking for classy, simple, elite all in one. We like dark blues/a little gold/yellow. Something that goes with our logo. We want our logo incorporated. Here is all the info you need:
Business name: RV Spine & Vitality Center
Location: 38915 North Bramble Ave
Palm Crest, FL 33488
Phone: 954-218-4630
Fax: 954-571-2846
Email: info@myrvspine.example

Names: Lucinda Ferrow, M.D.
Board Certified Hand and Upper Extremity Surgeon

Emeka Dlunga, M.D.
Board Certified Hip & Knee Replacement/General Orthopaedic Surgeon

Can decide what you want to put on the back. Maybe a slogan:
Steady in Healing. Built for You

I am just going to upload our logo. The only thing is if we select you as the winning design, the location, and phone numbers may change. We will need your help to update that once fully solidified.

Industry/Entity Type

Medical

Contact Information for Business Card

Colors
0054AA
0677BA
7BADD7
CADEEF
E8F1F8
0094D4
00A9DD
6FCCEA
C7EBF8
E9F6FB

Requirements
Must have
• class, appeal,
Should not have
• We want to air on the side of masculine if we are looking at masculine vs. feminine feel. But we still want it classy, sophisticated, and something we will love

```html
<!DOCTYPE html>
<html lang="en">
<head>
<meta charset="utf-8">
<title>RV Spine &amp; Vitality Center – Business Cards</title>
<link rel="stylesheet" href="https://fonts.googleapis.com/css2?family=Cinzel:wght@600&family=Libre+Caslon+Text:wght@700&family=Poppins:wght@400;500;600&display=swap">
<style>
  :root {
    --stage: #d3d3d3;
    --navy-deep: #0b2560;
    --navy: #0c3583;
    --royal-glow: #0a55b8;
    --white: #ffffff;
    --cyan: #1fb4e3;
    --gold-dark: #b8913a;
    --gold-light: #f4df8c;
    --divider: rgba(255,255,255,0.10);
  }
  * { box-sizing: border-box; margin: 0; padding: 0; }
  html, body { width: 1200px; height: 1200px; overflow: hidden; }
  body { background: var(--stage); position: relative; font-family: "Poppins", sans-serif; color: var(--white); }

  .card {
    position: absolute;
    left: 130px;
    width: 908px;
    height: 518px;
    background: radial-gradient(ellipse 52% 60% at 50% 42%, var(--royal-glow) 0%, var(--navy) 55%, var(--navy-deep) 100%);
    box-shadow: 0 6px 18px rgba(0,0,0,0.28);
    overflow: hidden;
  }
  .card--front { top: 60px; }
  .card--back { top: 620px; }

  .brand-name {
    position: absolute;
    left: 0; right: 0;
    text-align: center;
    font-family: "Cinzel", serif;
    font-weight: 600;
    color: var(--white);
    line-height: 1.15;
    letter-spacing: 1px;
  }
  .brand-mark {
    display: block;
    margin: 0 auto 14px;
    border-radius: 50%;
    border: 2px solid var(--white);
  }
  .card--front .brand-name { top: 118px; font-size: 44px; }
  .card--front .brand-mark { width: 62px; height: 62px; }
  .card--back .brand-name { top: 62px; font-size: 30px; }
  .card--back .brand-mark { width: 44px; height: 44px; margin-bottom: 10px; }

  .tagline {
    position: absolute;
    top: 341px; left: 0; right: 0;
    text-align: center;
    font-weight: 600;
    font-size: 29px;
    background: linear-gradient(90deg, var(--gold-dark), var(--gold-light) 55%, var(--gold-dark));
    -webkit-background-clip: text;
    background-clip: text;
    color: transparent;
  }
  .website {
    position: absolute;
    top: 408px; left: 0; right: 0;
    text-align: center;
    font-weight: 500;
    font-size: 22px;
    letter-spacing: 3px;
  }
  .website .domain { color: var(--cyan); font-weight: 600; }

  .physicians { position: absolute; left: 90px; top: 230px; width: 350px; }
  .physician + .physician { margin-top: 22px; }
  .physician__name {
    font-family: "Libre Caslon Text", serif;
    font-weight: 700;
    font-size: 27px;
    background: linear-gradient(90deg, var(--gold-dark), var(--gold-light) 60%, var(--gold-dark));
    -webkit-background-clip: text;
    background-clip: text;
    color: transparent;
    line-height: 1.2;
  }
  .physician__title { font-size: 17.5px; font-weight: 500; line-height: 1.3; margin-top: 6px; }

  .column-divider {
    position: absolute;
    left: 458px; top: 234px;
    width: 2px; height: 202px;
    background: var(--divider);
  }

  .contact { position: absolute; left: 522px; top: 228px; width: 370px; }
  .contact__practice {
    font-family: "Libre Caslon Text", serif;
    font-weight: 700;
    font-size: 19px;
    color: var(--cyan);
    line-height: 1.2;
    text-transform: uppercase;
    margin-bottom: 12px;
  }
  .contact__list { list-style: none; }
  .contact__item { display: flex; align-items: flex-start; font-size: 19px; line-height: 1.3; margin-bottom: 4px; }
  .contact__icon { width: 17px; height: 17px; margin: 5px 13px 0 6px; flex: none; fill: var(--gold-light); }
</style>
</head>
<body>

<section class="card card--front" aria-label="Card front">
  <div class="brand-name"><span class="brand-mark"></span>RV Spine &amp; Vitality<br>Center</div>
  <p class="tagline">Steady in Healing. Built for You</p>
  <p class="website">www.<span class="domain">myrvspine</span>.example</p>
</section>

<section class="card card--back" aria-label="Card back">
  <div class="brand-name"><span class="brand-mark"></span>RV Spine &amp; Vitality<br>Center</div>

  <div class="physicians">
    <div class="physician">
      <h2 class="physician__name">Lucinda Ferrow, M.D.</h2>
      <p class="physician__title">Board Certified Hand and Upper<br>Extremity Surgeon</p>
    </div>
    <div class="physician">
      <h2 class="physician__name">Emeka Dlunga, M.D.</h2>
      <p class="physician__title">Board Certified Hip &amp; Knee<br>Replacement/General</p>
    </div>
  </div>

  <div class="column-divider"></div>

  <div class="contact">
    <h3 class="contact__practice">RV Spine &amp;<br>Vitality Center</h3>
    <ul class="contact__list">
      <li class="contact__item">
        <svg class="contact__icon" viewBox="0 0 24 24"><path d="M6.6 10.8a15.1 15.1 0 0 0 6.6 6.6l2.2-2.2a1 1 0 0 1 1-.25 11.4 11.4 0 0 0 3.6.57 1 1 0 0 1 1 1V20a1 1 0 0 1-1 1A17 17 0 0 1 3 4a1 1 0 0 1 1-1h3.5a1 1 0 0 1 1 1c0 1.250.2 2.450.57 3.57a1 1 0 0 1-.25 1z"/></svg>
        954-218-4630
      </li>
      <li class="contact__item">
        <svg class="contact__icon" viewBox="0 0 24 24"><path d="M6 3h9v5H6zM4 9h16a1 1 0 0 1 1 1v10H3V10a1 1 0 0 1 1-1zm3 4v2h2v-2zm4 0v2h2v-2zm4 0v2h2v-2zm-8 3v2h2v-2zm4 0v2h2v-2zm4 0v2h2v-2z"/></svg>
        954-571-2846
      </li>
      <li class="contact__item">
        <svg class="contact__icon" viewBox="0 0 24 24"><path d="M2 5h20v14H2zm2 2v.5l8 5 8-5V7zm0 2.8V17h16V9.8l-8 5z"/></svg>
        info@myrvspine.example
      </li>
      <li class="contact__item">
        <svg class="contact__icon" viewBox="0 0 24 24"><path d="M12 2a7 7 0 0 0-7 7c0 5 7 13 7 13s7-8 7-13a7 7 0 0 0-7-7zm0 9.5A2.5 2.5 0 1 1 12 6.5a2.5 2.5 0 0 1 0 5z"/></svg>
        <span>38915 North Bramble Ave<br>Palm Crest, FL 33488</span>
      </li>
    </ul>
  </div>
</section>

</body>
</html>
```